Create Direct Mail Flyer For House Painting Company

The flyer needs to promote "Free Cheese For A Season" (When they paint their whole house. We want to Focus on the offer, also a free colour consultation, the awards and the guarantees! This will be a full colour 2 sided letter box drop flyer.
This is an emotional Direct Response flyer. I want the Headline to be Bold and stand out. Follow the branding if the website https://larkwoodresurfacing.com.au/
I have attached some social media photos to show you the promotion idea of Free Cheese For A Season. Use better photos if you have them.
I have given you a number of photos to use on the brochure, use your skills to determine what you feel is best to use. Also with the Colour consultation points use small photos to emphasise the points.
Have the testimonials and the team photo on the back.
Also have urgency. ACT NOW -OFFER ENDING SOON!

Target Market(s)

Home Owners

Industry/Entity Type

House Painting, Roof Painting

Colors
0054AA
0677BA
7BADD7
CADEEF
E8F1F8

Requirements
Must have
• Keep the Brand Colours. I have attached a sample flyer that shows a concept that I like. Have the testimonials on the back of the flyer. I do not want the flyer to look to busy.

```html
<!DOCTYPE html>
<html lang="en">
<head>
<meta charset="utf-8">
<title>Larkwood Home Transformations – Letterbox Flyer</title>
<link href="https://fonts.googleapis.com/css2?family=Bebas+Neue&family=Montserrat:wght@400;500;600;700&display=swap" rel="stylesheet">
<style>
:root{
  --blue-deep:#0677BA;
  --blue:#2AA3DC;
  --blue-mid:#4FB8E6;
  --blue-soft:#7BCBEF;
  --blue-pale:#CADEEF;
  --orange:#F7941D;
  --slate:#5F7681;
  --ink:#2B2B2B;
  --grey-bg:#C9C9C9;
  --card-grey:#EDEDED;
  --white:#FFFFFF;
}
*{box-sizing:border-box;margin:0;padding:0}
html,body{width:920px;height:1200px;overflow:hidden}
body{background:var(--grey-bg);font-family:"Montserrat",sans-serif;color:var(--ink);position:relative}
.sheet{position:absolute;top:297px;width:660px;height:930px;background:var(--white);transform-origin:0 0;transform:scale(.65);box-shadow:0 10px 24px rgba(0,0,0,.35);overflow:hidden}
.sheet--front{left:22px}
.sheet--back{left:469px}
.abs{position:absolute}
.photo{position:absolute}
.pill{display:inline-block;border-radius:999px;color:var(--white);font-weight:700;white-space:nowrap}
/* brand */
.brand{position:absolute;background:var(--white);text-align:center;color:var(--blue-deep);font-weight:600}
.brand__mark{display:block;margin:0 auto 8px;width:46px;height:46px;background:var(--blue-deep)}
.brand__name{display:block;font-size:24px;letter-spacing:1px;line-height:1;white-space:nowrap}
.brand__sub{display:block;font-size:12px;margin-top:5px;white-space:nowrap}
/* front */
.front-hero{left:0;top:0;width:660px;height:256px;background:linear-gradient(160deg,#7FA7C9 0%,#D9DEE2 45%,#5E7D52 100%)}
.front-product{left:462px;top:130px;width:150px;height:180px;background:linear-gradient(180deg,#F3D9A0,#E6B85A);border-radius:10px}
.front-band{left:0;top:256px;width:660px;height:260px;background:linear-gradient(180deg,var(--blue-soft),var(--blue))}
.front .brand{left:242px;top:189px;width:177px;height:133px;padding-top:22px}
.headline{left:0;top:338px;width:660px;text-align:center;font-family:"Bebas Neue",sans-serif;color:var(--white);font-size:52px;line-height:46px;font-weight:400}
.lede{left:50px;top:438px;width:560px;text-align:center;color:var(--white);font-size:13.5px;line-height:17px}
.lede b{font-weight:700}
.steps-title{left:0;top:502px;width:660px;text-align:center}
.steps-title .pill{background:var(--orange);font-size:15px;padding:4px 12px}
.steps-intro{left:0;top:538px;width:660px;text-align:center;font-size:13px}
.step{position:absolute;width:290px}
.step__num{position:absolute;left:-26px;top:-3px;font-size:18px;font-weight:700;color:var(--slate)}
.step__title{font-size:13px;font-weight:600;color:var(--blue);margin-bottom:10px}
.step__text{font-size:10.5px;line-height:13.5px;text-align:justify}
.front-foot{left:0;top:842px;width:660px;height:88px;background:linear-gradient(180deg,var(--blue-soft),var(--blue))}
.cta{left:96px;top:828px;display:flex}
.cta .pill{font-size:16px;padding:3px 10px}
.cta__call{background:var(--orange);border:2px solid var(--white)}
.cta__consult{background:var(--slate);border:2px solid var(--white);margin-left:-4px}
.phone-big{left:22px;top:868px;display:flex;align-items:center;color:var(--white);font-size:30px;font-weight:700;letter-spacing:.5px;white-space:nowrap}
.phone-big svg{margin-right:10px}
.foot-rule{left:308px;top:872px;width:2px;height:36px;background:var(--white)}
.foot-links{left:338px;top:868px;color:var(--white);font-size:10.5px;line-height:22px}
.foot-links div{display:flex;align-items:center;gap:10px}
/* back */
.back-hero{left:0;top:0;width:660px;height:302px;background:linear-gradient(180deg,#3F6FA8 0%,#9FB2C4 50%,#3E9BD1 100%)}
.back-band{left:0;top:302px;width:660px;height:140px;background:linear-gradient(180deg,var(--blue-soft),var(--blue))}
.offer-pill{left:0;top:292px;width:660px;text-align:center}
.offer-pill .pill{background:var(--orange);font-size:14.5px;padding:5px 14px}
.list{position:absolute;color:var(--white);font-size:11px}
.list__tag{display:inline-block;background:var(--white);color:var(--blue);font-weight:700;font-size:12.5px;border-radius:999px;padding:2px 10px;margin-bottom:7px}
.list li{list-style:none;display:flex;align-items:center;gap:6px;height:20px}
.divider{left:329px;top:330px;width:1px;height:106px;background:var(--white)}
.act{left:0;top:452px;width:660px;text-align:center;font-size:18px;font-weight:700;letter-spacing:.3px}
.review{position:absolute;width:282px;font-size:10px;line-height:12px;text-align:justify}
.review__who{color:var(--blue);font-weight:700;margin-top:5px;display:flex;gap:6px}
.stars{color:var(--orange);letter-spacing:1px}
.back-bar{left:0;top:718px;width:660px;height:32px;background:linear-gradient(180deg,var(--blue-soft),var(--blue));display:flex;align-items:center;gap:18px;padding-left:24px;color:var(--white);font-size:10.5px}
.back-bar span{display:flex;align-items:center;gap:4px}
.back-rest{left:0;top:750px;width:660px;height:180px;background:var(--card-grey)}
.back .brand{left:22px;top:772px;width:90px;background:transparent;padding:0}
.back .brand__mark{width:26px;height:26px;margin-bottom:4px}
.back .brand__name{font-size:14px}
.back .brand__sub{font-size:7px;margin-top:2px}
.stamp{left:576px;top:772px;width:60px;height:60px;background:var(--white)}
</style>
</head>
<body>

<section class="sheet sheet--front front">
  <div class="photo front-hero" role="img" aria-label="Photo of a freshly painted white weatherboard home with pool and garden"></div>
  <div class="photo front-band"></div>
  <div class="photo front-product" role="img" aria-label="Photo of a cheese platter for the free cheese offer"></div>

  <div class="brand">
    <span class="brand__mark"></span>
    <span class="brand__name">LARKWOOD</span>
    <span class="brand__sub">Home Transformations</span>
  </div>

  <h1 class="abs headline">Transform Your Home and<br>Sip on Free Cheese For A Season!</h1>
  <p class="abs lede">Paint your whole house with us and receive <b>a free colour consultation</b> to ensure the perfect shade. Plus, <b>enjoy a slice of cheese every day for a season</b>, on us. Our skilled painters are ready to transform your home.</p>

  <div class="abs steps-title"><span class="pill">"Four Steps to Bring Your Vision to Life!"</span></div>
  <p class="abs steps-intro">It is important to select the correct colours for your home.</p>

  <div class="step" style="left:50px;top:570px">
    <span class="step__num">1.</span>
    <h3 class="step__title">Consider the mood you want to create:</h3>
    <p class="step__text">Think about the atmosphere you want to evoke in each room. Do you want a calming and relaxing space, or a vibrant and energizing one? Choose colours that align with the mood you want to create.</p>
  </div>
  <div class="step" style="left:355px;top:570px">
    <span class="step__num">2.</span>
    <h3 class="step__title">Think about the room's function:</h3>
    <p class="step__text">Consider the purpose of each room and choose colours that align with the function. For instance, blue or green may be suitable for a bedroom to create a calming environment, while yellow or orange may work well in a kitchen to add warmth and energy.</p>
  </div>
  <div class="step" style="left:50px;top:690px">
    <span class="step__num">3.</span>
    <h3 class="step__title">Look at the room's natural light:</h3>
    <p class="step__text">Take note of the amount and direction of natural light in each room. Light affects how colours appear, so you'll want to choose shades that complement the lighting. For example, warm hues like red and orange work well in rooms with a lot of natural light, while cool hues like blue and green are better suited for rooms with less light.</p>
  </div>
  <div class="step" style="left:355px;top:690px">
    <span class="step__num">4.</span>
    <h3 class="step__title">Test the colours:</h3>
    <p class="step__text">Once you've narrowed down your choices, test them out in the room. Paint a small patch on the wall and observe how it looks at different times of the day and in different lighting conditions. This will help you determine if the colour is right for the space.</p>
  </div>

  <div class="photo front-foot"></div>
  <div class="abs cta"><span class="pill cta__call">Call Us Now</span><span class="pill cta__consult">For Your Free Colour Consultation</span></div>
  <div class="abs phone-big">
    <svg width="30" height="30" viewBox="0 0 30 30"><circle cx="15" cy="15" r="14" fill="var(--orange)" stroke="#fff" stroke-width="2"/><path d="M10 8c1-1 2 0 3 2s0 2-1 3c1 2 3 4 5 5 1-1 1-2 3-1s3 2 2 3-2 2-4 2c-5-1-10-6-10-11 0-1 1-2 2-3z" fill="#fff"/></svg>
    1300 555 018
  </div>
  <div class="abs foot-rule"></div>
  <div class="abs foot-links">
    <div><svg width="14" height="14" viewBox="0 0 14 14"><circle cx="7" cy="7" r="7" fill="#fff"/><rect x="3.5" y="4.5" width="7" height="5" fill="none" stroke="var(--blue)"/><path d="M3.5 4.5l3.5 3 3.5-3" fill="none" stroke="var(--blue)"/></svg>www.larkwoodresurfacing.com.au</div>
    <div><svg width="14" height="14" viewBox="0 0 14 14"><circle cx="7" cy="7" r="7" fill="#fff"/><circle cx="7" cy="7" r="4" fill="none" stroke="var(--blue)"/><path d="M3 7h8M7 3v8" stroke="var(--blue)"/></svg>admin@larkwoodresurfacing.com.au</div>
  </div>
</section>

<section class="sheet sheet--back back">
  <div class="photo back-hero" role="img" aria-label="Team photo of the painting crew standing with company vehicles outside the workshop"></div>
  <div class="photo back-band"></div>
  <div class="abs offer-pill"><span class="pill">Grab your free cheese and colour consultation while this offer lasts.</span></div>

  <div class="list" style="left:24px;top:332px">
    <span class="list__tag">Our Services</span>
    <ul>
      <li><svg width="10" height="10" viewBox="0 0 10 10"><path d="M1 5l3 3 5-6" fill="none" stroke="#fff" stroke-width="1.6"/></svg>Roof Restoration and Painting</li>
      <li><svg width="10" height="10" viewBox="0 0 10 10"><path d="M1 5l3 3 5-6" fill="none" stroke="#fff" stroke-width="1.6"/></svg>House Painting</li>
      <li><svg width="10" height="10" viewBox="0 0 10 10"><path d="M1 5l3 3 5-6" fill="none" stroke="#fff" stroke-width="1.6"/></svg>Epoxy Foors</li>
    </ul>
  </div>
  <div class="abs divider"></div>
  <div class="list" style="left:405px;top:332px">
    <span class="list__tag">Our Guarantees</span>
    <ul>
      <li><svg width="10" height="10" viewBox="0 0 10 10"><path d="M1 5l3 3 5-6" fill="none" stroke="#fff" stroke-width="1.6"/></svg>On Time Guarantee</li>
      <li><svg width="10" height="10" viewBox="0 0 10 10"><path d="M1 5l3 3 5-6" fill="none" stroke="#fff" stroke-width="1.6"/></svg>White Glove Cleanliness Guarantee</li>
      <li><svg width="10" height="10" viewBox="0 0 10 10"><path d="M1 5l3 3 5-6" fill="none" stroke="#fff" stroke-width="1.6"/></svg>15 Year Guarantee</li>
      <li><svg width="10" height="10" viewBox="0 0 10 10"><path d="M1 5l3 3 5-6" fill="none" stroke="#fff" stroke-width="1.6"/></svg>Satisfaction Guarantee</li>
    </ul>
  </div>

  <h2 class="abs act">ACT NOW -OFFER ENDING SOON!</h2>

  <div class="review" style="left:24px;top:490px">
    <p>Most professional painters we have ever dealt with from precision of work, tidiness, promptness, reliable company that followed up all queries immediately and with politeness at all times.</p>
    <p class="review__who">Maree Holloway <span class="stars">★★★★★</span></p>
  </div>
  <div class="review" style="left:354px;top:490px">
    <p>Recently had the exterior of my home and deck painted. The painters who came were very professional and friendly. Would not hesitate to recommend them for any painting requirements you might have.</p>
    <p class="review__who">Maree Holloway <span class="stars">★★★★★</span></p>
  </div>
  <div class="review" style="left:24px;top:580px">
    <p>Repaired and sealed my tile roof and repainted my water stained ceilings. Fast quote. fast turn around onthe job - in fact they got it done 2 weeks earlier than promised. Shane and team did a great job, were trust-worthy with full access to my home while I was at work and comms with admin were great Larkwood weren't my cheapest quote but were within 10% and what swung it for me was the 15year Coverall guarantee on the work Can certainly recommend.</p>
    <p class="review__who">Lorna P <span class="stars">★★★★★</span></p>
  </div>
  <div class="review" style="left:354px;top:580px">
    <p>Warren Tate and his team are true professionals. Warren sent his A team lead by Jensen to paint the interior and exterior of our new build. The attention to detail is exceptional, best paint team I have ever used. I would not hesitate to use them on all our uture projects and would not hesitate to recommend them. Thnx Larkwood team your super stats - not just 5 stars.</p>
    <p class="review__who">Colin Brandt <span class="stars">★★★★★</span></p>
  </div>

  <div class="abs back-bar">
    <span><svg width="10" height="10" viewBox="0 0 10 10"><path d="M2 1c1 0 2 2 2 3L3 5c1 1 1 2 2 2l1-1c1 0 3 1 3 2s-1 1-2 1C4 9 1 6 1 3c0-1 0-2 1-2z" fill="#fff"/></svg>1300 555 018</span>
    <span><svg width="10" height="10" viewBox="0 0 10 10"><circle cx="5" cy="5" r="4" fill="none" stroke="#fff"/><path d="M1 5h8M5 1v8" stroke="#fff"/></svg>www.larkwoodresurfacing.com.au</span>
    <span><svg width="10" height="10" viewBox="0 0 10 10"><rect x="1" y="2" width="8" height="6" fill="#fff"/><path d="M1 2l4 3 4-3" fill="none" stroke="var(--blue)"/></svg>admin@larkwoodresurfacing.com.au</span>
  </div>
  <div class="photo back-rest"></div>
  <div class="brand">
    <span class="brand__mark"></span>
    <span class="brand__name">LARKWOOD</span>
    <span class="brand__sub">Home Transformations</span>
  </div>
  <div class="abs stamp"></div>
</section>

</body>
</html>
```